Harbor Sushi & Steak Dinner Menu

I'm looking for a MENU design with a particular feel. I want to have a base template made that I can then use for future alterations to the menu; ie I can go in and change out different entrees as the menu changes but the template will remain the same. (Ideally it would be in an Apple Pages format.). Also ideally - dinner menu will occupy 2 pages 8.5 x 11. The restaurant's name is Harbor. It is a MODERN steak house that will also feature Sushi, a Raw Bar, Exquisite Cocktails and a sophisticated nightlife crowd. I have attached our LOGO, a secondary logo that we will be featuring throughout the project including on the menu cover (the gold U). Finally - I have attached the content that we would like to see. AGAIN - I REITERATE: High end dining and lounge atmosphere. A couple of restaurants / menus that I love are Morvendel in NYC and Pellucid Steakhouse in Long Island NY. Please do not duplicate - just trying to offer some suggestions.

Requirements
Must have
• A sophisticated and elegant feel without being stuffy or old.

```html
<!DOCTYPE html>
<html lang="en">
<head>
<meta charset="utf-8">
<title>Harbor Sushi &amp; Steak — Dinner Menu</title>
<link href="https://fonts.googleapis.com/css2?family=Lato:ital,wght@0,400;0,700;1,400&family=Josefin+Sans:wght@400&display=swap" rel="stylesheet">
<style>
  :root{
    --canvas:#ffffff;
    --page-black:#0b0b0b;
    --panel:#ffffff;
    --red:#e1262c;
    --red-dark:#8c1a1e;
    --gold:#d2a44c;
    --ink:#141414;
  }
  *{box-sizing:border-box;margin:0;padding:0}
  html,body{width:1200px;height:796px;overflow:hidden;background:var(--canvas)}
  body{position:relative;font-family:"Lato",Arial,sans-serif;color:var(--ink)}

  .menu-page{position:absolute;top:23px;width:573px;height:744px;background:var(--page-black);overflow:hidden}
  .menu-page--food{left:19px}
  .menu-page--kitchen{left:611px}
  .panel-shape{position:absolute;inset:0;width:573px;height:744px}

  .column{position:absolute;top:0;width:250px;height:640px}
  .at{position:absolute;left:0}

  .section-head{width:228px}
  .section-title{font-weight:400;font-size:14.5px;letter-spacing:.06em;color:var(--red);text-transform:uppercase;display:flex;align-items:center;gap:5px;line-height:14px;white-space:nowrap}
  .section-rule{height:5px;width:228px;margin-top:4px;
    background:repeating-linear-gradient(to bottom,var(--gold) 0 1px,transparent 1px 2px)}
  .gf{display:inline-block;width:8px;height:8px;border-radius:50%;background:var(--red);flex:none}

  .item-name{font-weight:700;font-size:10.3px;color:var(--gold);line-height:12px;display:flex;align-items:center;gap:3px;white-space:nowrap}
  .item-desc{font-style:italic;font-size:7.4px;line-height:10px;color:var(--ink);white-space:nowrap}

  .plain-list li{list-style:none;font-size:10.2px;line-height:16.9px;color:var(--ink);white-space:nowrap}
  .plain-list--tight li{line-height:16px}
  .raw-plate{font-size:10.2px;line-height:12px;white-space:nowrap}
  .raw-plate span{display:block;font-size:7.4px;line-height:10px}
  .platter-note{font-size:7.4px;font-style:italic;line-height:10px;white-space:nowrap}
  .single{font-size:10.2px;line-height:14px;white-space:nowrap}

  .sides li{list-style:none;font-size:10.2px;line-height:11.5px;margin-bottom:4.5px}
  .sides--main{width:165px}
  .sides--extra{width:80px}

  .brand{position:absolute;left:0;right:0;top:660px;display:flex;justify-content:center;align-items:center;gap:8px}
  .brand-name{font-family:"Josefin Sans",Arial,sans-serif;font-size:32px;letter-spacing:.12em;color:var(--gold);line-height:1}
  .brand-dot{width:8px;height:8px;border-radius:50%;background:var(--red)}
</style>
</head>
<body>

<section class="menu-page menu-page--food" aria-label="Sushi and raw bar page">
  <svg class="panel-shape" viewBox="0 0 573 744" aria-hidden="true">
    <polygon points="8,10 565,10 565,670 286,621 8,670" fill="none" stroke="var(--red-dark)" stroke-width="1"/>
    <polygon points="12,14 561,14 561,666 286,617 12,666" fill="var(--panel)" stroke="var(--red)" stroke-width="3"/>
  </svg>

  <div class="column" style="left:40px">
    <div class="at section-head" style="top:35px"><h2 class="section-title">Sushi / Sashimi <span class="gf"></span></h2><div class="section-rule"></div></div>
    <div class="at" style="top:65px"><div class="item-name">Toro</div><div class="item-desc">Blue Fin Tuna Belly</div></div>
    <div class="at" style="top:94px"><div class="item-name">Unagi</div><div class="item-desc">Fresh Water Eel</div></div>
    <div class="at" style="top:123px"><div class="item-name">Ebi</div><div class="item-desc">Cooked Shrimp</div></div>
    <div class="at" style="top:152px"><div class="item-name">Sake</div><div class="item-desc">Salmon</div></div>
    <div class="at" style="top:181px"><div class="item-name">Hamachi</div><div class="item-desc">Yellowtail</div></div>
    <div class="at" style="top:65px;left:110px"><div class="item-name">Madai</div><div class="item-desc">Red Snapper</div></div>
    <div class="at" style="top:94px;left:110px"><div class="item-name">Uni</div><div class="item-desc">Sea Urchin</div></div>
    <div class="at" style="top:123px;left:110px"><div class="item-name">Maguro</div><div class="item-desc">Tuna</div></div>
    <div class="at" style="top:152px;left:110px"><div class="item-name">Hirame</div><div class="item-desc">Fluke</div></div>

    <div class="at section-head" style="top:229px"><h2 class="section-title">Sushi Platters</h2><div class="section-rule"></div></div>
    <div class="at" style="top:258px"><div class="item-name">Small <span class="gf"></span></div><div class="item-desc">Five Pieces Assorted Sushi, Nine Pieces Sashimi, Spicy<br>Tuna Roll</div></div>
    <div class="at" style="top:297px"><div class="item-name">Large <span class="gf"></span></div><div class="item-desc">Eight Pieces Assorted Sushi, Eighteen Pieces Of<br>Sashimi, Alaskan Roll, Rainbow Roll</div></div>

    <div class="at section-head" style="top:356px"><h2 class="section-title">Classic Rolls</h2><div class="section-rule"></div></div>
    <div class="at" style="top:384px"><div class="item-name">Yellowtail <span class="gf"></span></div><div class="item-desc">Inside Out Roll With Scallions, Spicy Tuna or Salmon or Yellowtail,<br>Spicy Mayo</div></div>
    <div class="at" style="top:423px"><div class="item-name">California <span class="gf"></span></div><div class="item-desc">Crab Meat, Cucumber and Avocado</div></div>
    <div class="at" style="top:453px"><div class="item-name">Vegetable <span class="gf"></span></div><div class="item-desc">Avocado, Cucumber, Asparagus &amp; Pickled Reddish</div></div>
    <div class="at" style="top:482px"><div class="item-name">Spider</div><div class="item-desc">Soft Shell Crab &amp; Avocado With Eel Sauce</div></div>
    <div class="at" style="top:511px"><div class="item-name">Shrimp Tempura</div><div class="item-desc">Deep Fried Tempura Shrimp and Eel Sauce</div></div>
    <div class="at" style="top:541px"><div class="item-name">Alaskan <span class="gf"></span></div><div class="item-desc">Salmon and Avocado</div></div>
  </div>

  <div class="column" style="left:307px">
    <div class="at section-head" style="top:35px"><h2 class="section-title">Special Rolls</h2><div class="section-rule"></div></div>
    <div class="at" style="top:65px"><div class="item-name">The Harbor</div><div class="item-desc">Tuna, Salmon, Yellowtail, Avocado, Spicy Mayo, Soy Bean Paper</div></div>
    <div class="at" style="top:94px"><div class="item-name">King Crab Rainbow</div><div class="item-desc">King Crab, Avocado, Cucumbers, Assorted Fish on Top</div></div>
    <div class="at" style="top:122px"><div class="item-name">Empress</div><div class="item-desc">Shrimp Tempura, Spicy Tuna On Top, Eel Sauce, Spicy Mayo</div></div>
    <div class="at" style="top:151px"><div class="item-name">Spicy Girl</div><div class="item-desc">Spicy Crunchy Crab Meat, Cucumber, Shrimp on Top</div></div>
    <div class="at" style="top:179px"><div class="item-name">Dragon</div><div class="item-desc">Eel, Cucumber, Avocado, And Tobiko on Top, Eel Sauce</div></div>
    <div class="at" style="top:208px"><div class="item-name">Yummy</div><div class="item-desc">Spicy Crunchy Salmon, Avocado, Mango And Salmon on Top</div></div>
    <div class="at" style="top:237px"><div class="item-name">No. 9</div><div class="item-desc">Shrimp Tempura, Avocado, Kani, Spicy Mayo, Tobiko</div></div>
    <div class="at" style="top:266px"><div class="item-name">Sunrise Roll</div><div class="item-desc">Spicy Crunchy Tuna And Avocado, Spicy Crunchy Salmon on Top</div></div>

    <div class="at section-head" style="top:316px"><h2 class="section-title">Seafood Raw Bar</h2><div class="section-rule"></div></div>
    <ul class="at plain-list" style="top:343px">
      <li>Lobster Cocktail</li>
      <li>Shrimp Cocktail</li>
      <li>Clams on the Half Shell</li>
      <li>Oysters on the Half Shell</li>
      <li>Colossal Crab Cocktail</li>
    </ul>
    <div class="at raw-plate" style="top:432px">Raw Bar Plate for One<span>Two Shrimp, Half of a One Pound Lobster, Two Clams,<br>One East Coast Oyster, One West Coast Oyster</span></div>

    <div class="at section-head" style="top:488px"><h2 class="section-title">Seafood Platters <span class="gf"></span></h2><div class="section-rule"></div></div>
    <p class="at platter-note" style="top:519px">Shrimp, Oysters, Clams, Lobster and Crab</p>
    <p class="at single" style="top:537px">Large / Colossal</p>
  </div>

  <div class="brand"><span class="brand-dot"></span><span class="brand-name">HARBOR</span></div>
</section>

<section class="menu-page menu-page--kitchen" aria-label="Kitchen and steaks page">
  <svg class="panel-shape" viewBox="0 0 573 744" aria-hidden="true">
    <polygon points="8,10 565,10 565,670 286,621 8,670" fill="none" stroke="var(--red-dark)" stroke-width="1"/>
    <polygon points="12,14 561,14 561,666 286,617 12,666" fill="var(--panel)" stroke="var(--red)" stroke-width="3"/>
  </svg>

  <div class="column" style="left:39px">
    <div class="at section-head" style="top:33px"><h2 class="section-title">Appetizer</h2><div class="section-rule"></div></div>
    <div class="at" style="top:62px"><div class="item-name">BAO Bun</div><div class="item-desc">Hoisin BBQ Pancetta Cut Pork Loin, Crispy Onions, Micro Mint</div></div>
    <div class="at" style="top:92px"><div class="item-name">Five Spice Crispy Popcorn Crusted Prawns (2)</div><div class="item-desc">Classic Burre Blanc</div></div>
    <div class="at" style="top:121px"><div class="item-name">Jumbo Lump Crab</div><div class="item-desc">Citrus Miso Drizzle, Spring Pea Puree, Micro Greens</div></div>
    <div class="at" style="top:152px"><div class="item-name">Crispy Wonton Napoleon</div><div class="item-desc">Cucumber Gallete, Ahi Tuna, Jumbo Lump Crab Meat,<br>Wasabi Aioli, Shoestring Wontons</div></div>
    <div class="at" style="top:193px"><div class="item-name">PEI Mussels</div><div class="item-desc">Charred Artichoke Hearts, Blistered Heirloom Tomatoes, Garlic<br>White Wine Broth</div></div>
    <div class="at" style="top:234px"><div class="item-name">New Zealand / Domestic Small Eye Lamb Chop (1)</div><div class="item-desc">Crispy Porcini Risotto Cake</div></div>
    <div class="at" style="top:262px"><div class="item-name">Classic Wedge</div><div class="item-desc">Bleu Cheese, Bacon Lardons, Heirloom Tomatoes</div></div>
    <div class="at" style="top:291px"><div class="item-name">Mixed Baby Greens</div><div class="item-desc">Heirloom Tomatoes, Cucumber, Red Onion, Dijon Vinaigrette</div></div>
    <div class="at" style="top:320px"><div class="item-name">Tabulleh</div><div class="item-desc">Buckwheat Grain, Fresh Mint, Tomato Concasse, Cucumber,<br>Parsley, Fresh Squeezed Lemon, EVOO., Salt and Pepper</div></div>
    <div class="at" style="top:359px"><div class="item-name">Tomato Mozzarella Salad / Burratta</div></div>
    <div class="at" style="top:378px"><div class="item-name">Spinach Salad</div><div class="item-desc">Green Apple, Feta, Currants, with Per-simmons Vinaigrette</div></div>
    <div class="at" style="top:407px"><div class="item-name">Kale Caesar</div><div class="item-desc">Homemade Cacio E'peppe Dressing, Pecorino and Parmesan<br>Cheese, Toasted Croutons</div></div>

    <div class="at section-head" style="top:465px"><h2 class="section-title">Entrees</h2><div class="section-rule"></div></div>
    <div class="at" style="top:493px"><div class="item-name">Pan Roasted Miso Glazed Black Cod</div><div class="item-desc">Green Tea Noodle Stir Fry; Napa Cabbage, Carrot,<br>Japanese Eggplant</div></div>
    <div class="at" style="top:533px"><div class="item-name">Pan Seared Striped Bass</div><div class="item-desc">Lobster Succotash In A Tomato Saffron Broth</div></div>
    <div class="at" style="top:562px"><div class="item-name">E.V.O.O. Salted / Grilled Swordfish</div><div class="item-desc">Sun Dried Tomato, Olive and Caper Tapenade, Over Basmati Rice</div></div>
    <div class="at" style="top:591px"><div class="item-name">Grilled Half Chicken</div><div class="item-desc">Sun Dried Tomato And Basil Israeli Cous-cous, Pan Au Jus</div></div>
  </div>

  <div class="column" style="left:305px">
    <div class="at" style="top:32px"><div class="item-name">Roasted Fresh Caviatelle Ratatoille</div><div class="item-desc">Vegetable Broth</div></div>
    <div class="at" style="top:62px"><div class="item-name">Lobster Cartoccio</div><div class="item-desc">Shrimp, Mussels, Clams, Fresh Herb Tomato Broth, Tossed with<br>Bucatini</div></div>
    <div class="at" style="top:100px"><div class="item-name">Charred Artichoke Hearts <span class="gf"></span></div><div class="item-desc">Heirloom Tomatoes, Caper Berries, Spring Onions, Fresh Basil,<br>White Wine Reduction Over Forbidden Rice</div></div>
    <div class="at" style="top:139px"><div class="item-name">Mediterranean Grilled Veggie Plate <span class="gf"></span></div><div class="item-desc">Artichoke Hearts, Japanese Eggplant, Green &amp; White Asparagus,<br>Seared Heirloom Tomatoes, Roasted Baby Carrots, Cauliflower<br>Rice, Evoo &amp; Fig Drizzle</div></div>

    <div class="at section-head" style="top:210px"><h2 class="section-title">USDA Prime Steaks <span class="gf"></span></h2><div class="section-rule"></div></div>
    <ul class="at plain-list plain-list--tight" style="top:237px">
      <li>10 Oz Filet</li>
      <li>14 or 16 oz New York Strip</li>
      <li>24 oz Boneless Ribeye</li>
      <li>36 oz Bone in Rib Eye</li>
      <li>Berkshire Pork Chop</li>
    </ul>

    <div class="at section-head" style="top:340px"><h2 class="section-title">Sauces</h2><div class="section-rule"></div></div>
    <ul class="at plain-list plain-list--tight" style="top:367px">
      <li>Cabernet Demi Glaz</li>
      <li>Gorganzola Brulle Cream</li>
      <li>Truffled Wild Mushroom Ragu</li>
      <li>Horseradish Cream</li>
      <li>House Steak Sauce</li>
    </ul>

    <div class="at section-head" style="top:472px"><h2 class="section-title">Sides</h2><div class="section-rule"></div></div>
    <ul class="at sides sides--main" style="top:500px">
      <li>Mashed Idaho Potatoes</li>
      <li>Bacon, Sweet Corn, Caramelized Vidalia Onion fingerling potatoes</li>
      <li>Roasted Peanut Potatoes</li>
      <li>Creamed Spinach</li>
      <li>Sautéed Spinach</li>
      <li>Grilled Asparagus</li>
    </ul>
    <ul class="at sides sides--extra" style="top:500px;left:169px">
      <li>French Beans</li>
      <li>Israeli Cous Cous</li>
      <li>Sweet Potato Steak Fries</li>
      <li>Corn Skillet</li>
    </ul>
  </div>

  <div class="brand"><span class="brand-dot"></span><span class="brand-name">HARBOR</span></div>
</section>

</body>
</html>
```